Velvetorchid Hair & Beauty Business Card

Velvetorchid Hair & Beauty is a boutique salon located in the picturesque Lake Taupo NZ. The salon is very luxurious, opulent gold gilded mirrors, chandelier lit, contemporary french decor, sets the mood to create beautiful hair, makeup and all beauty services. Just had a new logo design and now after a new business card.
Logo
14 Korowhai Street
Taupo
Phone (07) 548 6193
www.velvetorchid.co.nz
email hair@velvetorchid.co.nz
Marlena Swithin
Also need a space to put in Stylist name, date, appointment time. thanks;)
Another idea is we could incorporate the wallpaper in the back ground either on the back or front or use an ornate glided frame (around the edge of the card) like on my website where my brides photos flash.
Decided against the wall paper but at least you can see our colour theme for the salon.
Updates

Please check out my updated brief . Thanks :)

Target Market(s)

25-60 years plus, mainly mid age females , wanting the best possible service , high standard of workmanship and money not a problem.

Industry/Entity Type

Boutique

Requirements
Must have
• Gold and silver

```html
<!DOCTYPE html>
<html lang="en">
<head>
<meta charset="utf-8">
<title>Velvetorchid Hair &amp; Beauty – Business Card Options</title>
<link rel="stylesheet" href="https://fonts.googleapis.com/css2?family=Montserrat:wght@400;700&display=swap">
<style>
  :root {
    --gold: #c9a25e;
    --taupe: #b5a394;
    --black: #141414;
    --ink: #2a2a2a;
    --rule: #dcbc84;
    --edge: #d4d4d4;
    --steel: #a8b8c4;
    --paper: #ffffff;
  }
  * { box-sizing: border-box; margin: 0; padding: 0; }
  html, body { width: 724px; height: 1200px; overflow: hidden; background: var(--paper); }
  body { position: relative; font-family: "Montserrat", Arial, sans-serif; color: var(--ink); }

  .option-label {
    position: absolute; left: 101px; width: 256px; text-align: center;
    font-weight: 700; font-size: 15px; letter-spacing: 0.5px; color: var(--black);
  }
  .option-label--one { top: 34px; }
  .option-label--two { top: 666px; }

  .card {
    position: absolute; width: 256px; height: 446px;
    background: var(--paper); border: 1px solid var(--edge); overflow: hidden;
  }
  .card--front { left: 101px; }
  .card--back { left: 381px; }
  .option-one .card { top: 67px; }
  .option-two .card { top: 699px; }

  /* striped bands on the front */
  .stripe-band {
    position: absolute; left: 0; right: 0; height: 53px;
    background: repeating-linear-gradient(90deg,
      var(--gold) 0 29px, var(--black) 29px 58px,
      var(--taupe) 58px 87px, var(--black) 87px 116px);
  }
  .stripe-band--top { top: 0; }
  .stripe-band--bottom { bottom: 0; }
  .band-rule { position: absolute; left: 0; right: 0; height: 3px; background: var(--steel); }
  .band-rule--top { top: 55px; }
  .band-rule--bottom { bottom: 56px; }
  .option-two .band-rule { background: var(--black); height: 2px; }

  /* salon name where the logo stands */
  .brand-name {
    position: absolute; left: 0; right: 0; top: 196px; text-align: center;
    font-family: "Montserrat", Arial, sans-serif; font-weight: 400;
    color: var(--gold); font-size: 18px; line-height: 26px;
  }

  /* back */
  .back-bar { position: absolute; left: 0; right: 0; height: 14px; background: var(--black); }
  .back-bar--top { top: 0; }
  .back-bar--bottom { bottom: 0; }

  .holder-name {
    position: absolute; left: 24px; font-weight: 700; font-size: 15px;
    letter-spacing: 0.5px; color: var(--black); white-space: nowrap;
  }
  .holder-name .surname { color: var(--taupe); }
  .option-one .holder-name { top: 124px; }
  .option-two .holder-name { top: 100px; }

  .write-line { position: absolute; left: 24px; width: 140px; height: 1px; background: var(--rule); }

  .contact {
    position: absolute; left: 24px; font-style: normal;
    font-size: 12px; line-height: 18px; color: var(--ink); white-space: nowrap;
  }
  .option-one .contact { top: 334px; }
  .option-two .contact { top: 138px; }

  .field-label { position: absolute; left: 24px; font-size: 11.5px; color: var(--ink); }
</style>
</head>
<body>

<section class="option option-one">
  <h2 class="option-label option-label--one">OPTION 1</h2>

  <div class="card card--front">
    <div class="stripe-band stripe-band--top"></div>
    <div class="band-rule band-rule--top"></div>
    <p class="brand-name">Velvetorchid<br>Hair &amp; Beauty</p>
    <div class="band-rule band-rule--bottom"></div>
    <div class="stripe-band stripe-band--bottom"></div>
  </div>

  <div class="card card--back">
    <p class="holder-name">MARLENA <span class="surname">SWITHIN</span></p>
    <div class="write-line" style="top:161px"></div>
    <div class="write-line" style="top:185px"></div>
    <div class="write-line" style="top:209px"></div>
    <div class="write-line" style="top:233px"></div>
    <div class="write-line" style="top:257px"></div>
    <address class="contact">
      14 Korowhai Street Taupo<br>
      (07) 548 6193<br>
      www.velvetorchid.co.nz<br>
      hair@velvetorchid.co.nz
    </address>
  </div>
</section>

<section class="option option-two">
  <h2 class="option-label option-label--two">OPTION 2</h2>

  <div class="card card--front">
    <div class="stripe-band stripe-band--top"></div>
    <div class="band-rule band-rule--top"></div>
    <p class="brand-name">Velvetorchid<br>Hair &amp; Beauty</p>
    <div class="band-rule band-rule--bottom"></div>
    <div class="stripe-band stripe-band--bottom"></div>
  </div>

  <div class="card card--back">
    <div class="back-bar back-bar--top"></div>
    <p class="holder-name">MARLENA <span class="surname">SWITHIN</span></p>
    <address class="contact">
      14 Korowhai Street Taupo<br>
      (07) 548 6193<br>
      www.velvetorchid.co.nz<br>
      hair@velvetorchid.co.nz
    </address>
    <p class="field-label" style="top:264px">Stylist</p>
    <div class="write-line" style="top:292px"></div>
    <div class="write-line" style="top:316px"></div>
    <p class="field-label" style="top:334px">Date &amp; Time</p>
    <div class="write-line" style="top:362px"></div>
    <div class="write-line" style="top:386px"></div>
    <div class="write-line" style="top:410px"></div>
    <div class="back-bar back-bar--bottom"></div>
  </div>
</section>

</body>
</html>
```